English and Spanish Language School Needs a Business Card

Need a business card design a startup company called Corvelle Language School. The company will offer English and Spanish conversational level courses designed to make the learner feel comfortable with grammar and vocabulary. We would like to see a logo with some colour that should communicate learning, growth.

Target Market(s)

Consumers and businesses

Industry/Entity Type

Education

Contact Information for Business Card

TBD

Font styles to use
Serif

Requirements
Must have
• Include the following
• Logo
• Name
• Title
• Cellphone Number
• Office Phone number
• Email address
• Office Address

```html
<!DOCTYPE html>
<html lang="en">
<head>
<meta charset="utf-8">
<title>Corvelle Language School – Business Card</title>
<link href="https://fonts.googleapis.com/css2?family=Open+Sans:wght@400;600;700;800&display=swap" rel="stylesheet">
<style>
  :root {
    --teal-light: #11c9cf;
    --teal: #06b3b9;
    --teal-dark: #05969c;
    --red: #c9232f;
    --white: #ffffff;
    --backdrop: #ece7df;
  }
  * { margin: 0; padding: 0; box-sizing: border-box; }
  html, body { width: 1200px; height: 1023px; overflow: hidden; }
  body {
    background: var(--backdrop);
    font-family: "Open Sans", Arial, sans-serif;
    position: relative;
  }
  .card {
    position: absolute;
    width: 560px;
    height: 320px;
    border-radius: 16px;
    background: radial-gradient(ellipse at 45% 35%, var(--teal-light) 0%, var(--teal) 55%, var(--teal-dark) 100%);
    box-shadow: 0 10px 24px rgba(0,0,0,0.18);
    overflow: hidden;
    color: var(--white);
  }
  .card-front { left: 70px; top: 120px; }
  .card-back { left: 570px; top: 583px; }

  .accent-band {
    position: absolute;
    right: 0; top: 0;
    width: 16px; height: 100%;
    background: var(--red);
  }

  .brand { position: absolute; line-height: 1; }
  .brand-name { font-weight: 800; letter-spacing: -1px; }
  .brand-tagline { font-weight: 400; margin-top: 4px; }

  .card-front .brand { left: 40px; top: 96px; color: var(--red); }
  .card-front .brand-name { font-size: 64px; }
  .card-front .brand-tagline { font-size: 20px; padding-left: 40px; }

  .holder { position: absolute; left: 250px; bottom: 40px; }
  .holder-name { font-size: 22px; font-weight: 700; }
  .holder-title { font-size: 12px; font-weight: 400; margin-top: 2px; }

  .contact-list {
    position: absolute;
    right: 36px; top: 40px;
    list-style: none;
    text-align: right;
    font-size: 12px;
    line-height: 1;
  }
  .contact-list li {
    display: flex;
    justify-content: flex-end;
    align-items: center;
    gap: 8px;
    margin-bottom: 9px;
  }
  .contact-list svg { width: 12px; height: 12px; flex: none; }

  .card-back .brand {
    left: 0; right: 0; top: 100px;
    text-align: center;
    color: var(--white);
  }
  .card-back .brand-row { display: inline-flex; align-items: center; gap: 12px; }
  .card-back .brand-name { font-size: 76px; }
  .brand-dot { width: 22px; height: 22px; border-radius: 50%; background: var(--red); margin-top: 22px; }
  .card-back .brand-tagline { font-size: 22px; }
</style>
</head>
<body>

<section class="card card-front">
  <div class="brand">
    <div class="brand-name">Corvelle</div>
    <div class="brand-tagline">Language School</div>
  </div>

  <ul class="contact-list">
    <li>55-204-71836
      <svg viewBox="0 0 12 12"><path d="M3 1 L5 3.5 L4 5 Q5 7 7 8 L8.5 7 L11 9 L10 11 Q4 11 1 2 Z" fill="#fff"/></svg>
    </li>
    <li>55-204-71835
      <svg viewBox="0 0 12 12"><rect x="3" y="0.8" width="6" height="10.4" rx="1" fill="none" stroke="#fff" stroke-width="1.2"/><circle cx="6" cy="9.4" r="0.7" fill="#fff"/></svg>
    </li>
    <li>info@corvelle-lang.com
      <svg viewBox="0 0 12 12"><rect x="0.8" y="2.5" width="10.4" height="7" fill="none" stroke="#fff" stroke-width="1.1"/><path d="M0.8 2.5 L6 6.5 L11.2 2.5" fill="none" stroke="#fff" stroke-width="1.1"/></svg>
    </li>
    <li>Your address
      <svg viewBox="0 0 12 12"><path d="M6 11.5 L2.6 6 A3.8 3.8 0 1 1 9.4 6 Z" fill="#fff"/><circle cx="6" cy="4.4" r="1.4" fill="#06b3b9"/></svg>
    </li>
  </ul>

  <div class="holder">
    <div class="holder-name">Your Name</div>
    <div class="holder-title">Title</div>
  </div>

  <div class="accent-band"></div>
</section>

<section class="card card-back">
  <div class="brand">
    <div class="brand-row">
      <span class="brand-name">Corvelle</span>
      <span class="brand-dot"></span>
    </div>
    <div class="brand-tagline">Language School</div>
  </div>
</section>

</body>
</html>
```